NJ TILL WORKS , CREDIT CARD PROCESSING EQUIPMENT

njtillworks is a sub division of Lumbar a credit car processing co.
dennis arlow
17 cedar hollow rd
warren nj 07133
suite 418

njtillworks.example
cell 555-261-0487
office 555-718-3306
we sell pos systems to merchant who want to accept credit cards at there retail location.
black card would be nice buit open to different ideas

Target Market(s)

retail merchants

Industry/Entity Type

credit card processing

Contact Information for Business Card

card should include web site phone address

Colors

Designer to choose colors to be used in the design.

Requirements
Should not have
• red

```html
<!DOCTYPE html>
<html lang="en">
<head>
<meta charset="utf-8">
<title>NJ Till Works — Business Card</title>
<link rel="stylesheet" href="https://fonts.googleapis.com/css2?family=Source+Sans+3:wght@400;600;700&display=swap">
<style>
  :root {
    --backdrop: #e4e4e4;
    --card: #1c1c1c;
    --ink: #f2f2f2;
    --accent: #e8b71a;
  }
  * { margin: 0; padding: 0; box-sizing: border-box; }
  html, body {
    width: 1200px;
    height: 960px;
    overflow: hidden;
    background: var(--backdrop);
    font-family: "Source Sans 3", sans-serif;
  }
  .card {
    position: absolute;
    left: 306px;
    width: 591px;
    height: 336px;
    background: var(--card);
    color: var(--ink);
  }
  .card--front { top: 123px; }
  .card--back { top: 511px; }

  .brand-name {
    position: absolute;
    font-weight: 600;
    color: var(--ink);
    white-space: nowrap;
    letter-spacing: 0.5px;
  }
  .card--front .brand-name {
    left: 0;
    right: 0;
    top: 152px;
    text-align: center;
    font-size: 47px;
    line-height: 1;
  }
  .tagline {
    position: absolute;
    left: 0;
    right: 0;
    top: 299px;
    text-align: center;
    font-size: 16.5px;
    line-height: 20px;
  }
  .tagline .company { color: var(--accent); }
  .tagline .company b { font-weight: 700; }

  .card--back .brand-name {
    left: 45px;
    top: 153px;
    font-size: 32px;
    line-height: 34px;
  }
  .divider {
    position: absolute;
    left: 294px;
    top: 116px;
    width: 2px;
    height: 105px;
    background: var(--ink);
  }
  .divider::before {
    content: "";
    position: absolute;
    left: 0;
    top: 0;
    width: 2px;
    height: 32px;
    background: var(--accent);
    border-bottom: 2px solid var(--card);
  }
  .contact {
    position: absolute;
    left: 334px;
    top: 115px;
  }
  .contact__name {
    color: var(--accent);
    font-weight: 700;
    font-size: 22px;
    line-height: 28px;
    margin-bottom: 17px;
  }
  .contact__line {
    display: flex;
    align-items: center;
    gap: 4px;
    font-size: 16px;
    line-height: 20px;
  }
  .contact__line svg { width: 13px; height: 13px; flex: none; }
  .address {
    position: absolute;
    left: 0;
    right: 0;
    top: 290px;
    text-align: center;
    font-size: 16px;
    line-height: 20px;
  }
</style>
</head>
<body>
  <section class="card card--front">
    <div class="brand-name">NJ TILL WORKS</div>
    <p class="tagline"><span class="company"><b>NJ</b>TillWorks</span> is a sub division of Lumbar a credit car processing co.</p>
  </section>

  <section class="card card--back">
    <div class="brand-name">NJ TILL WORKS</div>
    <div class="divider"></div>
    <div class="contact">
      <div class="contact__name">Dennis Arlow</div>
      <div class="contact__line">
        <svg viewBox="0 0 14 14" aria-hidden="true"><rect x="3.5" y="1" width="7" height="12" rx="1.2" fill="none" stroke="var(--accent)" stroke-width="1.3"/><line x1="6" y1="11" x2="8" y2="11" stroke="var(--accent)" stroke-width="1.2"/></svg>
        <span>555-261-0487</span>
      </div>
      <div class="contact__line">
        <svg viewBox="0 0 14 14" aria-hidden="true"><path d="M3 1.5 L5.2 1.5 L6 4.3 L4.6 5.5 Q5.8 8.2 8.5 9.4 L9.7 8 L12.5 8.8 L12.5 11 Q12.3 12.7 10.5 12.5 Q2 11.5 1.5 3.5 Q1.4 1.7 3 1.5 Z" fill="var(--accent)"/><path d="M8.5 1.8 Q11.8 2.3 12.2 5.6 M8.3 3.8 Q10 4.1 10.2 5.8" fill="none" stroke="var(--accent)" stroke-width="1"/></svg>
        <span>555-718-3306</span>
      </div>
      <div class="contact__line">
        <svg viewBox="0 0 14 14" aria-hidden="true"><g fill="none" stroke="var(--accent)" stroke-width="1.1"><circle cx="7" cy="7" r="5.8"/><ellipse cx="7" cy="7" rx="2.5" ry="5.8"/><line x1="1.2" y1="7" x2="12.8" y2="7"/><line x1="2" y1="4.2" x2="12" y2="4.2"/><line x1="2" y1="9.8" x2="12" y2="9.8"/></g></svg>
        <span>www.njtillworks.example</span>
      </div>
    </div>
    <p class="address">17 Cedar Hollow Rd, Suite 418, Warren NJ 07133</p>
  </section>
</body>
</html>
```